Business Card- Can you make it cool vs boring!

Need a refresh on my business card! Want it to be modern but simple, classic and a pop of coolness! we do senior living and it is boring. but that doesn't mean our business card have to look boring! Open to two sided cards. our website is www.Bruvel-HQ.com

Target Market(s)

capital market

Industry/Entity Type

senior housing/ real estate

Contact Information for Business Card

logo/ name/ cell/ address/ www.Bruvel-HQ.com/ space for a QR code

Requirements
Must have
• maybe a QR code (do not make prominent I may not use the QR so design where it can be taken out) that link to more about us/ landing page. needs to be modern but clean
Should not have
• clip art or script

```html
<!DOCTYPE html>
<html lang="en">
<head>
<meta charset="UTF-8">
<title>Bruvel Living – Business Card</title>
<link href="https://fonts.googleapis.com/css2?family=Poppins:wght@400;500&family=Satisfy&display=swap" rel="stylesheet">
<style>
  :root {
    --backdrop: #c6c6c6;
    --rust: #ad4f26;
    --rust-deep: #7c3516;
    --paper: #ffffff;
    --silver: #8a8a8f;
    --ink-light: #ffffff;
  }
  * { margin: 0; padding: 0; box-sizing: border-box; }
  html, body {
    width: 1200px; height: 1015px; overflow: hidden;
    background: var(--backdrop);
    font-family: "Poppins", sans-serif;
  }
  .card {
    position: absolute;
    width: 620px; height: 354px;
    overflow: hidden;
    box-shadow: 0 6px 14px rgba(0,0,0,0.35);
  }
  .card--front { left: 90px; top: 110px; background: var(--rust); }
  .card--back { left: 490px; top: 540px; background: var(--rust); }

  .brand {
    position: absolute;
    font-family: "Poppins", sans-serif;
    font-weight: 500;
    letter-spacing: 1px;
    white-space: nowrap;
  }
  .card--front .brand {
    left: 0; right: 0; top: 145px;
    text-align: center;
    font-size: 44px;
    color: var(--rust-deep);
  }
  .card--back .brand {
    left: 62px; top: 150px;
    font-size: 38px;
    color: var(--rust);
  }

  .back-art { position: absolute; inset: 0; }

  .contact {
    position: absolute;
    right: 26px; top: 120px;
    text-align: right;
    color: var(--ink-light);
  }
  .contact__name {
    font-family: "Satisfy", cursive;
    font-size: 30px;
    line-height: 1;
  }
  .contact__role { font-size: 13px; margin-bottom: 10px; }
  .contact__line {
    font-size: 13px; line-height: 19px;
    display: flex; justify-content: flex-end; align-items: center; gap: 6px;
  }
  .contact__line svg { width: 12px; height: 12px; }
  .contact__address { font-size: 13px; line-height: 18px; margin-top: 8px; }
</style>
</head>
<body>

<section class="card card--front" aria-label="Card front">
  <div class="brand">Bruvel Living</div>
</section>

<section class="card card--back" aria-label="Card back">
  <svg class="back-art" viewBox="0 0 620 354" aria-hidden="true">
    <path d="M0 0 H412 C380 110 352 240 318 300 C292 344 250 354 170 354 H0 Z" fill="var(--silver)"/>
    <path d="M0 0 H398 C366 110 340 240 306 298 C282 340 240 350 160 350 H0 Z" fill="var(--paper)"/>
    <path d="M0 0 H384 C354 110 328 236 294 290 C270 330 228 338 150 338 H0 Z" fill="var(--paper)" stroke="var(--paper)"/>
    <path d="M378 0 C350 110 322 230 290 284 C266 324 226 332 150 330" fill="none" stroke="var(--silver)" stroke-width="5"/>
  </svg>

  <div class="brand">Bruvel Living</div>

  <div class="contact">
    <div class="contact__name">Marcus Hale</div>
    <div class="contact__role">Managing Director</div>
    <div class="contact__line">044-210 987 654
      <svg viewBox="0 0 12 12"><path d="M2 1 L4.5 1 L5.5 3.5 L4 4.6 C4.7 6.2 5.8 7.3 7.4 8 L8.5 6.5 L11 7.5 L11 10 C6 10.5 1.5 6 2 1 Z" fill="var(--ink-light)"/></svg>
    </div>
    <div class="contact__line">info@bruvelmail.com
      <svg viewBox="0 0 12 12"><rect x="0.5" y="2.5" width="11" height="7" fill="var(--ink-light)"/><path d="M0.5 2.5 L6 7 L11.5 2.5" fill="none" stroke="var(--rust)" stroke-width="1"/></svg>
    </div>
    <div class="contact__line">www.Bruvel-HQ.com
      <svg viewBox="0 0 12 12"><circle cx="6" cy="6" r="5.2" fill="var(--ink-light)"/><path d="M1 6 H11 M6 1 V11 M6 1 C3.5 3.5 3.5 8.5 6 11 M6 1 C8.5 3.5 8.5 8.5 6 11" fill="none" stroke="var(--rust)" stroke-width="0.8"/></svg>
    </div>
    <div class="contact__address">421, Address line goes here<br>45452, Country Name</div>
  </div>
</section>

</body>
</html>
```